Business Card - Rebranding for Consulting Firm

We are renaming and rebranding our consulting firm and need to raise the level of quality of our cards as part of that effort. We consult to leading high tech, life science and other innovation sector companies.

Need a two-sided business card design.

Side 1: (a) Company logo (b) tag line: Optimize Your Investment in Talent (c) Name (d) Title (e) Phone 1: Office (f) Phone 2: Mobile (g) email: person@HollowmereAdvisory.com

Side 2: Two lines of text: (a) Growth is Imperative. Change is Constant. Talent Executes Strategy. (b) We help you excel at all three.

Target Market(s)

Business and human resources executives and senior managers

Industry/Entity Type

Management Consulting

Contact Information for Business Card

Font styles to use
Sans Serif

Requirements
Must have
• clean, not too busy, but with a bit of creativity. Stick to the colors used in the attached logo
• appeal to high tech, life science companies
Nice to have
• prefer white background

```html
<!DOCTYPE html>
<html lang="en">
<head>
<meta charset="utf-8">
<title>Hollowmere Advisory – Business Card</title>
<link rel="stylesheet" href="https://fonts.googleapis.com/css2?family=Open+Sans:wght@300;400;600&display=swap">
<style>
  :root {
    --bg: #e9ebee;
    --card-white: #ffffff;
    --brand-blue: #0b6fae;
    --brand-navy: #1d3f78;
    --tag-blue: #1f8fd6;
    --ink-gray: #6b7078;
    --rule-gray: #b9bec5;
    --back-text: #d9e6f2;
  }
  * { box-sizing: border-box; margin: 0; padding: 0; }
  html, body { width: 1200px; height: 892px; overflow: hidden; }
  body {
    background: var(--bg);
    font-family: "Open Sans", Arial, sans-serif;
    display: flex;
    align-items: center;
    justify-content: center;
    gap: 60px;
  }
  .card {
    width: 520px;
    height: 297px;
    position: relative;
    box-shadow: 0 10px 28px rgba(0,0,0,0.14);
  }
  .card-front { background: var(--card-white); }
  .brand {
    position: absolute;
    top: 46px;
    right: 36px;
    display: flex;
    align-items: center;
    gap: 10px;
  }
  .brand-mark {
    width: 22px;
    height: 22px;
    background: var(--brand-blue);
  }
  .brand-name {
    font-size: 26px;
    font-weight: 600;
    color: var(--brand-navy);
    letter-spacing: -0.3px;
  }
  .tagline {
    position: absolute;
    top: 92px;
    right: 36px;
    font-size: 17px;
    font-weight: 400;
    color: var(--tag-blue);
  }
  .person {
    position: absolute;
    top: 44px;
    left: 36px;
  }
  .person-name {
    font-size: 18px;
    font-weight: 600;
    color: var(--brand-navy);
    letter-spacing: 1.5px;
    text-transform: uppercase;
  }
  .person-title {
    font-size: 12px;
    color: var(--ink-gray);
    margin-top: 2px;
  }
  .contact {
    position: absolute;
    left: 200px;
    bottom: 36px;
    border-left: 1px solid var(--rule-gray);
    padding-left: 22px;
    display: flex;
    flex-direction: column;
    gap: 9px;
  }
  .contact-row {
    display: flex;
    align-items: center;
    gap: 12px;
    font-size: 11.5px;
    color: var(--ink-gray);
  }
  .contact-row svg { width: 16px; height: 16px; flex: none; }
  .card-back {
    background: var(--brand-blue);
    display: flex;
    flex-direction: column;
    align-items: center;
    justify-content: center;
    gap: 16px;
    text-align: center;
    text-transform: uppercase;
    color: var(--back-text);
  }
  .back-statement { font-size: 10.5px; letter-spacing: 0.6px; font-weight: 400; }
  .back-promise { font-size: 12.5px; letter-spacing: 0.8px; font-weight: 600; }
</style>
</head>
<body>
  <section class="card card-front" aria-label="Business card front">
    <div class="person">
      <p class="person-name">Your Name</p>
      <p class="person-title">Title</p>
    </div>
    <div class="brand">
      <span class="brand-mark"></span>
      <span class="brand-name">Hollowmere Advisory</span>
    </div>
    <p class="tagline">Optimize Your Investment in Talent</p>
    <div class="contact">
      <div class="contact-row">
        <svg viewBox="0 0 16 16" aria-hidden="true"><rect x="1" y="5" width="14" height="10" rx="1.5" fill="var(--brand-blue)"/><rect x="3" y="1.5" width="10" height="3" rx="1" fill="var(--brand-blue)"/><rect x="4" y="7" width="8" height="2" fill="#fff"/><circle cx="5" cy="12" r="1" fill="#fff"/><circle cx="8" cy="12" r="1" fill="#fff"/><circle cx="11" cy="12" r="1" fill="#fff"/></svg>
        <span>+1 555 010 4477</span>
      </div>
      <div class="contact-row">
        <svg viewBox="0 0 16 16" aria-hidden="true"><rect x="4" y="1" width="8" height="14" rx="1.5" fill="none" stroke="var(--brand-blue)" stroke-width="1.6"/><circle cx="8" cy="12.3" r="0.9" fill="var(--brand-blue)"/></svg>
        <span>+1 555 010 4477</span>
      </div>
      <div class="contact-row">
        <svg viewBox="0 0 16 16" aria-hidden="true"><text x="8" y="13" text-anchor="middle" font-family="Open Sans, sans-serif" font-size="15" font-weight="600" fill="var(--brand-blue)">@</text></svg>
        <span>person@HollowmereAdvisory.com</span>
      </div>
    </div>
  </section>

  <section class="card card-back" aria-label="Business card back">
    <p class="back-statement">Growth is imperative. Change is constant. Talent executes strategy.</p>
    <p class="back-promise">We help you excel at all three</p>
  </section>
</body>
</html>
```